Design a business card size Fridge Magnet

A property development company based in Sydney, Australia requires a fridge magnet to be designed. This will be mailed to landowners in the area so it must be eye-catching and 'friendly' but still professional so that these property owners won't mind having it on their fridge. Please refer to the document entitled "Brookmoor_FridgeMagnet_Brief.pdf" which is attached.

Target Market(s)

Land/Property owners in northwest sydney.

Industry/Entity Type

Business

Requirements
Must have
• My project must contain the information as displayed in the sample design shown in the brief.

```html
<!DOCTYPE html>
<html lang="en">
<head>
<meta charset="utf-8">
<title>Brookmoor Property Developers – Fridge Magnet</title>
<link rel="stylesheet" href="https://fonts.googleapis.com/css2?family=Montserrat:wght@400;600;700&family=Roboto+Condensed:wght@400;700&display=swap">
<style>
  :root {
    --band-top: #3f8088;
    --teal-text: #1b7f96;
    --brand-dark: #23272b;
    --brand-line: #1f8aa6;
    --band-blue: #1e8aa6;
    --stripe-teal: #35a89b;
    --pale: #e3f2f3;
    --accent-red: #d7141c;
    --ink: #161616;
    --white: #ffffff;
    --bg: #ffffff;
  }
  * { margin: 0; padding: 0; box-sizing: border-box; }
  html, body { width: 1200px; height: 736px; overflow: hidden; background: var(--bg); }
  .magnet {
    position: relative;
    width: 1200px; height: 736px;
    background: linear-gradient(180deg, var(--white) 0%, var(--white) 28%, var(--pale) 52%);
    font-family: "Roboto Condensed", "Arial Narrow", sans-serif;
    overflow: hidden;
  }
  .top-band { position: absolute; left: 0; top: 0; width: 100%; height: 40px; background: var(--band-top); }

  .brand { position: absolute; left: 0; right: 0; top: 70px; display: flex; flex-direction: column; align-items: center; }
  .brand-row { display: flex; align-items: center; gap: 22px; }
  .brand-square { width: 52px; height: 52px; background: var(--stripe-teal); }
  .brand-name {
    font-family: "Montserrat", sans-serif; font-weight: 400; font-size: 66px;
    letter-spacing: 2px; color: var(--brand-dark); line-height: 1;
  }
  .brand-tag {
    margin-top: 10px; margin-left: 74px; display: flex; align-items: center; gap: 14px;
    font-family: "Montserrat", sans-serif; font-size: 19px; letter-spacing: 2px; color: var(--brand-dark);
  }
  .brand-tag::before, .brand-tag::after { content: ""; width: 44px; height: 3px; background: var(--brand-line); }

  .questions { position: absolute; left: 0; right: 0; top: 200px; list-style: none; text-align: center; }
  .questions li {
    font-weight: 700; font-size: 30px; color: var(--teal-text); line-height: 48px;
    display: flex; justify-content: center; align-items: center; gap: 14px;
  }
  .questions .arrow { width: 0; height: 0; border-top: 11px solid transparent; border-bottom: 11px solid transparent; }
  .questions .arrow.right { border-left: 16px solid var(--stripe-teal); }
  .questions .arrow.left { border-right: 16px solid var(--stripe-teal); }

  .wave { position: absolute; left: 0; top: 340px; width: 1200px; height: 140px; }

  .portrait {
    position: absolute; left: 0; top: 325px; width: 290px; height: 250px;
    background: linear-gradient(160deg, #cfd9dd 0%, #9fb0b8 55%, #2e3338 100%);
  }

  .offer {
    position: absolute; left: 290px; top: 380px; width: 600px;
    font-weight: 700; font-size: 29px; line-height: 44px; color: var(--ink);
  }
  .offer .hl, .ps .hl { color: var(--accent-red); font-weight: 700; }

  .gift-card {
    position: absolute; left: 890px; top: 345px; width: 215px; height: 135px;
    border-radius: 10px; transform: rotate(5deg);
    background: linear-gradient(135deg, #ffffff 0%, #e8eeea 100%);
    box-shadow: 0 2px 6px rgba(0,0,0,.25);
  }

  .contact-band {
    position: absolute; left: 0; top: 475px; width: 100%; height: 100px; background: var(--band-blue);
    display: flex; align-items: center; color: var(--white); font-family: "Montserrat", sans-serif;
  }
  .contact-name { margin-left: 320px; font-weight: 700; font-size: 42px; }
  .contact-phone { margin-left: 66px; font-size: 42px; font-weight: 400; }
  .contact-phone strong { font-weight: 700; }

  .stripe { position: absolute; left: 0; top: 575px; width: 100%; height: 20px; background: var(--stripe-teal); }

  .bottom { position: absolute; left: 0; top: 595px; width: 100%; height: 141px; background: var(--white); }
  .voucher-badge {
    position: absolute; left: 58px; top: 48px; width: 150px; height: 62px; border-radius: 6px;
    background: linear-gradient(180deg, #e0262c, #b50f16); color: var(--white);
    transform: rotate(-3deg); box-shadow: 0 2px 4px rgba(0,0,0,.3);
    text-align: center; font-family: "Roboto Condensed", sans-serif;
  }
  .voucher-badge .amount { display: block; font-size: 30px; line-height: 34px; margin-top: 2px; }
  .voucher-badge .label { display: block; font-size: 16px; font-style: italic; line-height: 18px; }
  .ps {
    position: absolute; left: 290px; top: 38px; width: 880px;
    font-size: 25px; line-height: 38px; color: var(--ink);
  }
</style>
</head>
<body>
<main class="magnet">
  <div class="top-band"></div>

  <header class="brand">
    <div class="brand-row">
      <span class="brand-square"></span>
      <span class="brand-name">BROOKMOOR</span>
    </div>
    <div class="brand-tag">PROPERTY DEVELOPERS</div>
  </header>

  <ul class="questions">
    <li><span class="arrow right"></span>Are you considering selling your property?<span class="arrow left"></span></li>
    <li><span class="arrow right"></span>Is your lot size greater than ½ acre (2,000 m²)?<span class="arrow left"></span></li>
    <li><span class="arrow right"></span>Does your land have development potential?<span class="arrow left"></span></li>
  </ul>

  <svg class="wave" viewBox="0 0 1200 140" preserveAspectRatio="none" aria-hidden="true">
    <path d="M0 40 C 300 -10, 700 -10, 1200 50 L1200 140 L0 140 Z" fill="#ffffff"/>
  </svg>

  <div class="portrait" role="img" aria-label="Portrait photo of Daniel Ashford, the contact person, in a suit"></div>

  <p class="offer">If so, contact me now and receive a <span class="hl">$50 gift<br>card</span> when we meet to discuss your property!</p>

  <div class="gift-card" role="img" aria-label="Greenmart gift card with a green ribbon bow"></div>

  <section class="contact-band">
    <span class="contact-name">Daniel Ashford</span>
    <span class="contact-phone"><strong>Mobile:</strong> (0400) 555-218</span>
  </section>

  <div class="stripe"></div>

  <footer class="bottom">
    <div class="voucher-badge">
      <span class="amount">$500</span>
      <span class="label">Gift Voucher</span>
    </div>
    <p class="ps">P.S. If you know anyone else who is selling their property, we will give you a<br><span class="hl">$500 voucher</span> for passing on their name to us (if we acquire the property).</p>
  </footer>
</main>
</body>
</html>
```